Kelvora Supply Export Company web

We need a web design for an existing website we have. we want it to be simple yet flashy. It's a simple 3 page informative website with a link to our email address and line card. First page would be to introduce the company. second page would be the list of items we carry and third would be the contact page. I would like SEO optimization.
I would like a black background for the Webpage with flash and SEO optimization.
Reason: Need more information need it to be SEO
It Company

```html
<!DOCTYPE html>
<html lang="en">
<head>
<meta charset="utf-8">
<title>TQS Supply – Kelvora Supply Export Company</title>
<link href="https://fonts.googleapis.com/css2?family=Oswald:wght@500;600&family=Noto+Sans:wght@400;700&family=Arimo:wght@400;700&display=swap" rel="stylesheet">
<style>
:root{
  --page-bg:#000000;
  --map-glow:#1a1a1a;
  --blue-dark:#0d3f63;
  --blue-mid:#1d6a94;
  --blue-light:#2f89b6;
  --panel:#fbfbfb;
  --text:#3a3a3a;
  --heading:#505050;
  --headline:#9aa4ad;
  --brand-light:#e8e8e8;
  --footer-text:#d9d9d9;
}
*{margin:0;padding:0;box-sizing:border-box}
html,body{width:1200px;height:819px;overflow:hidden}
body{background:var(--page-bg);font-family:"Noto Sans",sans-serif;color:var(--text);position:relative}
.world-map{position:absolute;left:0;top:0;width:1200px;height:370px;background:radial-gradient(ellipse at 50% 40%,var(--map-glow),transparent 70%)}
.site{position:absolute;left:189px;top:0;width:823px}
.brand{position:absolute;left:25px;top:46px;display:flex;align-items:center;gap:8px;font-weight:700;font-size:22px;color:var(--brand-light);letter-spacing:.5px}
.brand-mark{width:18px;height:18px;background:var(--blue-light)}
.header-shape{position:absolute;left:0;top:32px}
.nav{position:absolute;left:491px;top:32px;display:flex;height:84px}
.nav a{display:flex;align-items:center;justify-content:center;color:#fff;text-decoration:none;font-family:"Noto Sans",sans-serif;font-size:13px;border-left:1px solid #0f4a70;text-shadow:0 1px 1px #0a2f48}
.nav a:nth-child(1){width:104px}
.nav a:nth-child(2){width:113px}
.nav a:nth-child(3){width:115px}
.banner{position:absolute;left:0;top:116px;width:823px;height:186px;overflow:hidden}
.banner-visual{position:absolute;inset:0 0 17px 0;background:radial-gradient(circle at 50% 110%,#2b8ac0 0%,#155f8f 45%,#0c3d66 100%)}
.banner-strip{position:absolute;left:0;bottom:0;width:100%;height:17px;background:linear-gradient(#2a7fae,#1a6391);border-top:1px solid #0b3a5c;border-bottom:2px solid #0b3a5c}
.tagline{position:absolute;left:17px;top:17px;width:384px;height:124px;border:1px solid rgba(255,255,255,.12);border-radius:6px;background:rgba(10,50,85,.35);padding:9px 16px}
.tagline h1{font-family:Oswald,sans-serif;font-weight:600;font-size:28px;line-height:36px;letter-spacing:.4px;color:var(--headline);text-transform:uppercase;white-space:nowrap}
.enquiry{position:absolute;left:575px;top:15px;width:238px;height:65px;border:1px solid rgba(255,255,255,.15);border-radius:6px;background:rgba(10,45,80,.55);display:flex;align-items:center;padding-left:12px;gap:8px;color:#c9d3dc}
.enquiry .label{font-family:Oswald,sans-serif;font-size:15px;line-height:16px}
.enquiry .phone{font-family:Oswald,sans-serif;font-size:15px;line-height:17px}
.enquiry .email{font-size:10px;font-weight:700}
.content{position:absolute;left:0;top:302px;width:823px;height:427px;background:linear-gradient(#fff 80%,#e9e9e9);border-radius:0 0 14px 14px}
.intro{position:absolute;left:30px;top:27px}
.intro h2{font-family:Arimo,sans-serif;font-size:18px;color:var(--heading);font-weight:700;width:331px;padding-bottom:5px;border-bottom:1px dashed #b9b9b9}
.intro p{font-size:10.6px;line-height:15.4px;width:440px;margin-top:15.4px}
.intro h2 + p{margin-top:20px}
.intro p.wide{width:560px;margin-top:23px}
.gallery{position:absolute;left:622px;top:22px}
.photo-frame{width:168px;height:130px;padding:6px;background:#fff;border:1px solid #d6d6d6;border-radius:4px;box-shadow:0 1px 3px rgba(0,0,0,.15);margin-bottom:18px}
.photo{width:100%;height:100%}
.photo.crate{background:linear-gradient(#c9b487,#a48a5b)}
.photo.rolls{background:linear-gradient(#7c95ad,#cfd2d6 60%,#7d7e80)}
.footer-links{position:absolute;left:195px;top:766px;font-family:Arimo,sans-serif;font-size:11px;font-weight:700;color:var(--footer-text)}
.footer-links a{color:inherit;text-decoration:none}
.footer-links .sep{margin:0 14px;font-weight:400;color:#777}
.copyright{position:absolute;left:195px;top:787px;font-family:Arimo,sans-serif;font-size:11px;color:var(--footer-text)}
.footer-brand{position:absolute;left:906px;top:768px;font-size:16px;font-weight:700;color:#9a9a9a}
</style>
</head>
<body>
<div class="world-map" role="img" aria-label="Dotted world map background"></div>

<div class="site">
  <div class="brand"><span class="brand-mark"></span>TQS SUPPLY</div>

  <svg class="header-shape" width="823" height="84" viewBox="0 0 823 84" aria-hidden="true">
    <defs>
      <linearGradient id="navGrad" x1="0" y1="0" x2="0" y2="1">
        <stop offset="0" stop-color="#2f84b0"/>
        <stop offset="1" stop-color="#175c87"/>
      </linearGradient>
    </defs>
    <path d="M290 84 C380 80 410 70 450 35 C480 8 495 0 520 0 L808 0 Q823 0 823 15 L823 84 Z" fill="url(#navGrad)"/>
  </svg>

  <nav class="nav">
    <a href="#">Home</a>
    <a href="#">Services</a>
    <a href="#">Contact</a>
  </nav>

  <section class="banner">
    <div class="banner-visual" role="img" aria-label="Blue globe with flight routes and aircraft"></div>
    <div class="banner-strip"></div>
    <div class="tagline">
      <h1>We export<br>construction materials,<br>computer, trucks etc.</h1>
    </div>
    <div class="enquiry">
      <svg width="54" height="40" viewBox="0 0 54 40" aria-hidden="true">
        <path d="M2 12 Q27 -2 52 12 L52 18 L42 18 L40 12 Q27 8 14 12 L12 18 L2 18 Z" fill="#8fa3b6"/>
        <path d="M10 20 L44 20 L50 38 L4 38 Z" fill="#8fa3b6"/>
        <circle cx="27" cy="29" r="6" fill="#143f62"/>
      </svg>
      <div>
        <div class="label">for enquires</div>
        <div class="phone">222-300-574</div>
        <div class="email">Email: info@kelvorasupply.com</div>
      </div>
    </div>
  </section>

  <main class="content">
    <div class="intro">
      <h2>Welcome to TQS Supply.</h2>
      <p>Pellentesque condimentum dui quis sem fermentum a mattis ipsum ultrices. Integer eu lacus sit amet mauris hendrerit egestas et eget neque.</p>
      <p>Lorem ipsum dolor sit amet, consectetur adipiscing elit. Pellentesque condimentum dui quis sem fermentum a mattis ipsum ultrices. Integer eu lacus sit amet mauris hendrerit egestas et eget neque. Mauris ac justo tempus velit imperdiet placerat. Nullam dolor lectus, sollicitudin sed dictum nec, consequat in erat. Quisque nibh ligula</p>
      <p>Integer eu lacus mauris hendrerit egestas imperdiet placerat ullam dolor lectus sollicitudin sed dictum uisque nibh ligula, pharetra sit amet euismod.</p>
      <p class="wide">At Norwell Trading Limited Integer eu lacus mauris hendrerit egestas imperdiet placerat ullam dolor lectus sollicitudin sed dictum uisque nibh ligula, pharetra sit amet euismod. Pellentesque condimentum dui quis sem fermentum a mattis ipsum ultrices. Integer eu lacus sit amet mauris hendrerit egestas et eget neque. Mauris ac justo tempus velit imperdiet placerat. Nullam dolor lectus, sollicitudin sed dictum nec, consequat in erat. Quisque nibh ligula</p>
    </div>
    <div class="gallery">
      <div class="photo-frame"><div class="photo crate" role="img" aria-label="Wooden shipping crate in a warehouse"></div></div>
      <div class="photo-frame"><div class="photo rolls" role="img" aria-label="Wrapped rolls of conveyor belting outside a depot"></div></div>
    </div>
  </main>
</div>

<div class="footer-links">
  <a href="#">Home</a><span class="sep">|</span><a href="#">About us</a><span class="sep">|</span><a href="#">Services</a><span class="sep">|</span><a href="#">Privacy Policy</a><span class="sep">|</span><a href="#">Sitemap</a><span class="sep">|</span><a href="#">Contact us</a>
</div>
<div class="copyright">Copyright © 2012 TQS Supply LTD. All right reserved.</div>
<div class="footer-brand">TQS SUPPLY</div>
</body>
</html>
```